Large Banner Poster for Entrance required by Beach Club

We are a beach club ( www. k o r a l s h o r e.ae) and we need a sign design to replace the one we currently have (pictured) which is getting old.

Please bear in mind the following details:
1 - This is the first thing guests see before they arrive at reception and therefore must shape their expectations for the pricing and rules/regulations of the club.
2 - The poster is in direct sunlight for at least 14 hours a day and so we would want any design to be as fade-resistant as possible in the choice of colors - darker colors fade less than brighter ones.
3 - The poster is 5.1m wide and 2.6m high. It will be printed on thick canvas.

I have attached a design of an internal sign we have for rules and regulations to give you an idea of the style we prefer. We do not need this sign to be in arabic.

We need the sign to convey the following information, the layout can be however you like:

-
Please Adhere to the Rules at ALL times:
No Swimming when the red flag is raised
No Swimming near the rocks, breakwater or outside the safe zone
No Swimming after sunset
All swimmers must wear appropriate swimwear
Children are the responsibility of accompanying adults
Outside food & drink are prohibited
Please comply with staff instructions at all times
Respect the beach and help us to keep it clean
All guests enter the beach at their own risk
-
Along the bottom should be:
Management Accepts no Liability for any loss or injury suffered - Use of the Beach is strictly at your own risk
-
All of our contact details (instagram, email, website, twitter, bbm, kik etc) should be as the new sign in the photo and placed in a similar manner (20140521_104544.jpg)
-
Admission Fees:
Admission Weekday Weekend/Public Holiday
Adult (16+) 50AED 100AED
Youth (8-16) 25AED 50AED
Child (under 8) F R E E
Cabanas Available on request

Entry includes a Towel, Sunbed and Parasol (subject to availability), ask about Membership today, rates start at only 350AED per month.

-

Industry/Entity Type

Club

```html
<!DOCTYPE html>
<html lang="en">
<head>
<meta charset="utf-8">
<title>Koral Shore – Entrance Banner</title>
<link href="https://fonts.googleapis.com/css2?family=Arimo:wght@400;700&family=Archivo+Narrow:wght@700&family=Comfortaa:wght@700&display=swap" rel="stylesheet">
<style>
  :root {
    --sky: #8ccbee;
    --sky-light: #e6f4fb;
    --palm: #3f7a2a;
    --palm-dark: #23491b;
    --trunk: #8a5a2e;
    --sand: #e9d6b4;
    --sea: #3fc2cf;
    --panel: rgba(255, 255, 255, 0.86);
    --ink: #2b2b2b;
    --alert: #e4202a;
    --footer-bg: #ffffff;
    --footer-ink: #222222;
    --bullet: #1c5f8c;
    --brand: #ffffff;
  }
  * { box-sizing: border-box; margin: 0; padding: 0; }
  html, body { width: 1200px; height: 611px; overflow: hidden; background: #fff; }
  .banner {
    position: relative;
    width: 1200px;
    height: 611px;
    font-family: "Arimo", Arial, sans-serif;
    color: var(--ink);
    overflow: hidden;
  }
  .scene {
    position: absolute;
    left: 0; top: 0;
    width: 1200px; height: 541px;
    background:
      radial-gradient(ellipse 420px 300px at 130px 330px, rgba(138, 90, 46, 0.85), transparent 70%),
      radial-gradient(ellipse 700px 260px at 600px 40px, rgba(35, 73, 27, 0.9), transparent 70%),
      radial-gradient(ellipse 380px 240px at 1080px 60px, rgba(63, 122, 42, 0.85), transparent 70%),
      linear-gradient(180deg, transparent 70%, rgba(233, 214, 180, 0.95) 92%),
      linear-gradient(90deg, var(--palm-dark) 0%, var(--trunk) 22%, var(--sky) 45%, var(--sky-light) 75%, var(--sea) 100%);
  }
  .brand {
    position: absolute;
    left: 40px; top: 55px;
    width: 330px;
    color: var(--brand);
    font-family: "Comfortaa", "Arimo", sans-serif;
    font-weight: 700;
    line-height: 0.95;
  }
  .brand__top { display: block; font-size: 92px; letter-spacing: 2px; }
  .brand__bottom { display: block; font-size: 80px; letter-spacing: 6px; padding-left: 20px; margin-top: 26px; }
  .panel {
    position: absolute;
    background: var(--panel);
    border-radius: 8px;
  }
  .panel--entry {
    left: 336px; top: 301px; width: 340px; height: 60px;
    padding: 6px 12px 0 14px;
    font-size: 12px; line-height: 1.42;
  }
  .panel--fees {
    left: 336px; top: 373px; width: 340px; height: 131px;
    padding: 7px 12px 0 14px;
    font-size: 14px; line-height: 1.44;
  }
  .panel--rules {
    left: 722px; top: 249px; width: 408px; height: 259px;
    padding: 12px 14px 0 14px;
  }
  .panel__title {
    color: var(--alert);
    font-weight: 700;
    font-size: 14.5px;
    margin-bottom: 2px;
  }
  .panel--rules .panel__title { font-size: 13.8px; margin-bottom: 6px; }
  .rules { list-style: none; font-size: 14px; line-height: 1.24; }
  .rules li { position: relative; padding-left: 15px; margin-bottom: 4.3px; }
  .rules li::before {
    content: ""; position: absolute; left: 2px; top: 6px;
    width: 5px; height: 5px; border-radius: 50%; background: var(--bullet);
  }
  .deco { position: absolute; border-radius: 50%; }
  .deco--sun { left: 1082px; top: 226px; width: 68px; height: 68px; background: #f7c62a; }
  .deco--melon { left: 655px; top: 303px; width: 34px; height: 22px; background: #e94b4b; border-radius: 0 0 34px 34px; }
  .deco--drink { left: 290px; top: 381px; width: 44px; height: 82px; background: #5cc7e8; border-radius: 8px 8px 20px 20px; }
  .deco--popsicle { left: 705px; top: 368px; width: 24px; height: 54px; background: #f07b5a; border-radius: 12px; }
  .deco--ring { left: 614px; top: 452px; width: 70px; height: 54px; background: #f25b7a; }
  .deco--star { left: 550px; top: 472px; width: 32px; height: 32px; background: #f4a23a; }
  .deco--flipflops { left: 1090px; top: 446px; width: 68px; height: 60px; background: #e84a8c; border-radius: 30px; }
  .liability {
    position: absolute;
    left: 0; top: 516px; width: 1200px;
    padding-left: 335px;
    font-family: "Archivo Narrow", "Arial Narrow", sans-serif;
    font-weight: 700;
    font-size: 14.4px;
    color: var(--alert);
    text-transform: uppercase;
    white-space: nowrap;
  }
  .footer {
    position: absolute;
    left: 0; top: 541px;
    width: 1200px; height: 70px;
    background: var(--footer-bg);
    color: var(--footer-ink);
  }
  .contacts {
    position: absolute; left: 0; top: 8px; width: 1200px; height: 28px;
    font-size: 16.5px;
  }
  .contact { position: absolute; top: 0; display: flex; align-items: center; height: 28px; white-space: nowrap; }
  .contact__dot { width: 26px; height: 26px; border-radius: 50%; background: var(--bullet); margin-right: 12px; }
  .website {
    position: absolute; left: 0; top: 46px; width: 1200px;
    text-align: center; padding-left: 4px;
    font-weight: 700; font-size: 17px; letter-spacing: 3.5px;
  }
</style>
</head>
<body>
<main class="banner">
  <div class="scene" role="img" aria-label="Tropical beach photograph with leaning palm trees, blue sky and turquoise sea"></div>

  <h1 class="brand"><span class="brand__top">KORAL</span><span class="brand__bottom">shore</span></h1>

  <section class="panel panel--entry">
    <p>Entry includes a Towel, Sunbed and Parasol<br>(subject to availability), ask about Membership today,<br>rates start at only 350AED per month.</p>
  </section>

  <section class="panel panel--fees">
    <h2 class="panel__title">ADMISSION FEES</h2>
    <p>Admission Weekday Weekend/Public Holiday</p>
    <p>Adult (16+) 50AED 100AED</p>
    <p>Youth (8-16) 25AED 50AED</p>
    <p>Child (under 8) F R E E</p>
    <p>Cabanas Available on request</p>
  </section>

  <section class="panel panel--rules">
    <h2 class="panel__title">PLEASE ADHERE TO THE RULES AT ALL TIMES</h2>
    <ul class="rules">
      <li>No Swimming when the red flag is raised</li>
      <li>No Swimming near the rocks, breakwater or<br>outside the safe zone</li>
      <li>No Swimming after sunset</li>
      <li>All swimmers must wear appropriate swimwear</li>
      <li>Children are the responsibility of accompanying adults</li>
      <li>Outside food &amp; drink are prohibited</li>
      <li>Please comply with staff instructions at all times</li>
      <li>Respect the beach and help us to keep it clean</li>
      <li>All guests enter the beach at their own risk</li>
    </ul>
  </section>

  <div class="deco deco--sun" role="img" aria-label="Sun sticker illustration"></div>
  <div class="deco deco--melon" role="img" aria-label="Watermelon slice sticker illustration"></div>
  <div class="deco deco--drink" role="img" aria-label="Cocktail glass sticker illustration"></div>
  <div class="deco deco--popsicle" role="img" aria-label="Ice lolly sticker illustration"></div>
  <div class="deco deco--ring" role="img" aria-label="Swim ring sticker illustration"></div>
  <div class="deco deco--star" role="img" aria-label="Starfish sticker illustration"></div>
  <div class="deco deco--flipflops" role="img" aria-label="Flip flops sticker illustration"></div>

  <p class="liability">Management accepts no liability for any loss or injury suffered - use of the beach is strictly at your own risk</p>

  <footer class="footer">
    <div class="contacts">
      <span class="contact" style="left:173px"><span class="contact__dot"></span>@koralshore</span>
      <span class="contact" style="left:314px"><span class="contact__dot"></span>@koralshore</span>
      <span class="contact" style="left:469px"><span class="contact__dot"></span>connect.koralshore.ae</span>
      <span class="contact" style="left:697px"><span class="contact__dot"></span>64219375</span>
      <span class="contact" style="left:862px"><span class="contact__dot"></span>info@koralshore.ae</span>
    </div>
    <p class="website">www.koralshore.ae</p>
  </footer>
</main>
</body>
</html>
```